Australian Independent Feature Film SPITE needs poster design

Here is the story of the film: SPITE tells the story of an Indian man named Kal who gets deeper and deeper involved in the Australian gangland underworld. He becomes close to his mentor The Lamplighter Otto and becomes emotionally involved with Otto's niece Tessa. His relationship with Tessa makes him an enemy of Max, Tessa's "partner" and Otto's right hand man. Kal only wants to get enough money to go back to homeland to rescue his parents from abject poverty, but is forced by Otto and Tessa to make increasing difficult decisions that go against what's left of his conscience. His confrontations with Max don't help. How far is too far when one tries to reach his noble goal? SPITE is an epic film tribute to Gerald Hume Wexley's The Lamplighter, a story of family relationships, intrigues and betrayals set against a violent world where nothing is legal, but where everything is possible.

The attached photos are to give you inspiration to create the poster. There is also attached a word document that includes the film credits that need to be in the poster.

Target Market(s)

international English speaking audiences. The poster should be very classy and appeal to audiences who like very artistic and something different in their films - not the usual commercial superhero films that are flooding the market now. I've attached some film posters from The Lamplighter, Ironjaw and other films as references.

Industry/Entity Type

Film Production

Font styles to use
Other font styles liked:
• HYPMoKGaK-Bold-Italics for Main Title SPITE is an option, but not absolutely necessary. The font seems to have bullet holes through it and is torn along edges.

Colors

Designer to choose colors to be used in the design.

Requirements
Must have
• There is attached a word document that includes the film credits that need to be in the poster.
Nice to have
• images that are highly dramatic and eye catching
Should not have
• Should not have any images that include nudity. This should be a poster for all audiences.

```html
<!DOCTYPE html>
<html lang="en">
<head>
<meta charset="utf-8">
<title>SPITE — Poster</title>
<link href="https://fonts.googleapis.com/css2?family=Special+Elite&family=Roboto+Condensed:wght@500;700&display=swap" rel="stylesheet">
<style>
  :root {
    --olive-light: #b3ac82;
    --olive-mid: #8c875c;
    --olive-dark: #5c5a3a;
    --figure-light: #7b7454;
    --figure-dark: #262720;
    --title-white: #fbfaf5;
    --credit-white: #f3f1e8;
  }
  html, body {
    margin: 0;
    padding: 0;
    overflow: hidden;
    background: var(--olive-dark);
  }
  .poster {
    position: relative;
    width: 810px;
    height: 1200px;
    overflow: hidden;
    background:
      radial-gradient(ellipse 55% 40% at 50% 40%, var(--olive-light) 0%, rgba(179,172,130,0) 75%),
      radial-gradient(ellipse 110% 85% at 50% 45%, var(--olive-mid) 35%, var(--olive-dark) 100%);
  }
  .portrait {
    position: absolute;
    left: 0;
    top: 190px;
    width: 810px;
    height: 760px;
  }
  .title {
    position: absolute;
    top: 82px;
    left: 0;
    width: 810px;
    margin: 0;
    text-align: center;
    font-family: "Special Elite", "Courier New", monospace;
    font-size: 176px;
    line-height: 1;
    letter-spacing: 22px;
    text-indent: 22px;
    color: var(--title-white);
    -webkit-text-stroke: 7px var(--title-white);
    text-shadow: 0 3px 8px rgba(40,38,20,0.45);
  }
  .billing {
    position: absolute;
    left: 0;
    top: 950px;
    width: 810px;
    text-align: center;
    font-family: "Roboto Condensed", "Arial Narrow", sans-serif;
    color: var(--credit-white);
  }
  .billing-presents {
    margin: 0 0 12px;
    font-weight: 700;
    font-size: 24px;
    letter-spacing: 0.4px;
  }
  .billing-block {
    width: 670px;
    margin: 0 auto;
    font-weight: 700;
    font-size: 13.5px;
    line-height: 23px;
    letter-spacing: 0.2px;
    text-transform: uppercase;
  }
  .billing-block span { margin: 0 5px; }
</style>
</head>
<body>
  <div class="poster">
    <svg class="portrait" viewBox="0 0 810 760" role="img" aria-label="Portrait photograph of the lead actor in a dark suit and bow tie, fading into the olive background">
      <defs>
        <linearGradient id="figureTone" x1="0" y1="0" x2="0" y2="1">
          <stop offset="0" stop-color="var(--figure-light)" stop-opacity="0.85"/>
          <stop offset="0.55" stop-color="var(--figure-dark)" stop-opacity="0.75"/>
          <stop offset="0.85" stop-color="var(--figure-dark)" stop-opacity="0.55"/>
          <stop offset="1" stop-color="var(--figure-dark)" stop-opacity="0"/>
        </linearGradient>
      </defs>
      <path d="M190 40 Q190 0 240 0 L570 0 Q620 0 620 40 L620 470 L810 560 L810 760 L0 760 L0 560 L190 470 Z" fill="url(#figureTone)"/>
    </svg>

    <h1 class="title">SPITE</h1>

    <div class="billing">
      <p class="billing-presents">VANTA PICTURES PTY LTD &amp; MBT PRODUCTIONS PTY LTD PRESENT</p>
      <p class="billing-block">
        <span>A Dane-Marie Holt Film Spite</span>
        <span>Starring Rafiq Nair</span>
        <span>Colin Ashby</span>
        <span>Clara Voss</span>
        <span>Terry D'Amato</span>
        <span>Martin Keller</span>
        <span>Zoe Hart</span>
        <span>Jean-Luc Berne</span>
        <span>Kiki Thomas</span>
        <span>Marina Holden</span>
        <span>Producers Rafiq Nair &amp; Dane-Marie Holt</span>
        <span>Associate Producers Edward Pinner &amp; Soyun Park Holt</span>
        <span>Director of Photography &amp; Film Editor Owen Carlton</span>
        <span>Post-Production Supervisor Neil Fitz-Morgan</span>
        <span>Re-Recording Mixer &amp; Sound Design Simon Pearce</span>
        <span>Music Composer Nicholas O'Brien</span>
        <span>Production Design Fiona McAllister</span>
        <span>Costume Design Leilani Watts</span>
        <span>Makeup &amp; Hair Design Elena Papadakis</span>
        <span>Casting MBT Productions Pty Ltd</span>
        <span>Screenplay Graham Ashcroft</span>
        <span>Directed by Dane-Marie Holt</span>
      </p>
    </div>
  </div>
</body>
</html>
```